Morrow Engineering Core Values Branding Package

Morrow Engineering has recently refined its company Core Values and is seeking a strong, cohesive branding package to visually bring these values to life. The new graphic assets will communicate our commitment to excellence in a way that resonates with our team, clients, and partners in a blue-collar, industrial environment.

We are looking for multiple visual assets with consistent design elements that can be applied across platforms. The tone should reflect strength, reliability, and professionalism while remaining approachable and aligned with our industry.

Core Values & Descriptions
Accountability
“We take ownership of our work and actions, ensuring reliability and trust in every solution we deliver.”

Teamwork
“We collaborate across departments and disciplines to provide the highest level of service and innovation for our clients.”

Integrity
“We operate with honesty, transparency, and ethical standards in all aspects of our business.”

Growth
“We are committed to continuous improvement—of our people, our processes, and our impact in the industry.”

Deliverables

1. Primary Core Values Graphic
A master visual representing all four values together.
Designed for use on posters, office signage, internal presentations.

2. Individual Value Graphics (x4)
One graphic per core value: Accountability, Teamwork, Integrity, Growth.
Cohesive style with slight visual variation to reflect each value’s unique meaning.

Target Market(s)

Employees of Morrow Engineering

Industry/Entity Type

Blue Collar

Font styles to use
Sans Serif

Colors
0054AA
0677BA
7BADD7
CADEEF
E8F1F8
00AB8E
00BBA5
67D7C9
C6EFE9
E9F9F6
EB3D1F
EC4F4E
F09395
F8D3D4
FCEDEE

Requirements
Must have
• Accountability, Teamwork, Integrity, Growth

```html
<!DOCTYPE html>
<html lang="en">
<head>
<meta charset="utf-8">
<title>Morrow Engineering — Core Values</title>
<link href="https://fonts.googleapis.com/css2?family=Roboto+Condensed:wght@400;700;800&display=swap" rel="stylesheet">
<style>
  :root {
    --navy: #0b2a5c;
    --green: #36a33b;
    --red: #d51a2e;
    --yellow: #f7b114;
    --ink: #1d1d1f;
    --dots: #a6a6a6;
    --paper: #ffffff;
    --backdrop: #e4e4e4;
  }
  html, body {
    margin: 0;
    padding: 0;
    width: 1200px;
    height: 1200px;
    overflow: hidden;
    background: var(--backdrop);
    font-family: "Roboto Condensed", "Arial Narrow", sans-serif;
  }
  .poster {
    position: absolute;
    left: 143px;
    top: 0;
    width: 914px;
    height: 1200px;
    background: var(--paper);
    overflow: hidden;
  }
  .wordmark {
    position: absolute;
    left: 0;
    right: 0;
    top: 96px;
    margin: 0;
    text-align: center;
    font-weight: 800;
    font-size: 76px;
    line-height: 1;
    letter-spacing: 1px;
    color: var(--navy);
  }
  .headline {
    position: absolute;
    left: 0;
    right: 0;
    top: 266px;
    margin: 0;
    text-align: center;
    font-weight: 800;
    font-size: 98px;
    line-height: 1;
    color: var(--navy);
    letter-spacing: 0.5px;
  }
  .tag {
    position: absolute;
    height: 55px;
    display: flex;
    align-items: center;
    justify-content: center;
    color: #fff;
    font-weight: 700;
    font-size: 42px;
    border-radius: 14px 0 14px 0;
    letter-spacing: -0.5px;
  }
  .tag--people { left: 80px; top: 372px; width: 369px; background: var(--navy); }
  .tag--solutions { left: 464px; top: 372px; width: 369px; background: var(--green); }
  .tag--now { left: 310px; top: 441px; width: 293px; background: var(--red); }

  .value { position: absolute; width: 200px; }
  .value h2 {
    margin: 0;
    font-weight: 800;
    font-size: 42px;
    line-height: 1;
    white-space: nowrap;
  }
  .value p {
    margin: 28px 0 0;
    font-size: 17px;
    line-height: 24.5px;
    letter-spacing: -0.2px;
    color: var(--ink);
    white-space: nowrap;
  }
  .value--accountability { left: 80px; top: 556px; }
  .value--accountability h2 { color: var(--yellow); }
  .value--teamwork { right: 81px; top: 556px; text-align: right; }
  .value--teamwork h2 { color: var(--green); }
  .value--growth { left: 80px; top: 782px; }
  .value--growth h2 { color: var(--red); }
  .value--integrity { right: 81px; top: 782px; text-align: right; }
  .value--integrity h2 { color: var(--navy); }

  .leader {
    position: absolute;
    border-top: 3px dotted var(--dots);
  }
  .leader--drop { border-top: none; border-left: 3px dotted var(--dots); }
  .leader--acc { left: 80px; top: 606px; width: 247px; }
  .leader--acc-drop { left: 324px; top: 606px; height: 34px; }
  .leader--team { left: 591px; top: 606px; width: 242px; }
  .leader--team-drop { left: 591px; top: 606px; height: 34px; }
  .leader--growth { left: 80px; top: 833px; width: 196px; }
  .leader--integrity { left: 636px; top: 833px; width: 197px; }

  .values-wheel {
    position: absolute;
    left: 285px;
    top: 600px;
    width: 344px;
    height: 344px;
  }
  .closing {
    position: absolute;
    left: 80px;
    top: 1060px;
    margin: 0;
    font-size: 25px;
    line-height: 33px;
    color: var(--green);
  }
</style>
</head>
<body>
  <main class="poster">
    <div class="wordmark">MORROW</div>

    <h1 class="headline">CORE VALUES</h1>

    <div class="tag tag--people">The Right People</div>
    <div class="tag tag--solutions">The Right Solutions</div>
    <div class="tag tag--now">Right Now!</div>

    <section class="value value--accountability">
      <h2>Accountability</h2>
      <p>We take ownership of our<br>work and actions, ensuring<br>reliability and trust in every<br>solution we deliver.</p>
    </section>
    <div class="leader leader--acc"></div>
    <div class="leader leader--drop leader--acc-drop"></div>

    <section class="value value--teamwork">
      <h2>Teamwork</h2>
      <p>We collaborate across<br>departments and disciplines<br>to provide the highest level<br>of service and innovation for<br>our clients.</p>
    </section>
    <div class="leader leader--team"></div>
    <div class="leader leader--drop leader--team-drop"></div>

    <section class="value value--growth">
      <h2>Growth</h2>
      <p>We are committed to<br>continuous improvement—of<br>our people, our processes, and<br>our impact in the industry.”</p>
    </section>
    <div class="leader leader--growth"></div>

    <section class="value value--integrity">
      <h2>Integrity</h2>
      <p>We operate with honesty,<br>transparency, and ethical<br>standards in all aspects of<br>our business.</p>
    </section>
    <div class="leader leader--integrity"></div>

    <svg class="values-wheel" viewBox="0 0 344 344" role="img"
         aria-label="Four-piece puzzle circle with icons for accountability, teamwork, growth and integrity">
      <path d="M166 166 H0 A166 166 0 0 1 166 0 Z" fill="var(--yellow)"/>
      <path d="M178 166 V0 A166 166 0 0 1 344 166 Z" fill="var(--green)"/>
      <path d="M166 178 V344 A166 166 0 0 1 0 178 Z" fill="var(--red)"/>
      <path d="M178 178 H344 A166 166 0 0 1 178 344 Z" fill="var(--navy)"/>
    </svg>

    <p class="closing">Be a bright part of our organization.<br>Become involved and demonstrate<br>you have the right stuff.</p>
  </main>
</body>
</html>
```